Letterhead Design for Law Firm that Specializes in Property Damage Litigation

We are looking for a redesign of our letterhead. Our current letterhead lists all of our current staff members and we'd like to come up with a design that does NOT list all of the staff members so that it does not need to be updated with every newly hired employee. Must be in editable format.

We are a law firm that specializes in property damage, so we need something that is professional, yet modern. The final design should use our existing logo and should use a blue color scheme (alternate colors would be gray, black, and white).

Industry/Entity Type

Legal

Colors
0054AA
0677BA
7BADD7
CADEEF
E8F1F8

```html
<!DOCTYPE html>
<html lang="en">
<head>
<meta charset="utf-8">
<title>Hartwell Osten &amp; Marlowe — Letterhead</title>
<link href="https://fonts.googleapis.com/css2?family=Lato:wght@400;700&family=Montserrat:wght@500;700&display=swap" rel="stylesheet">
<style>
  :root {
    --backdrop: #b9b9b9;
    --paper: #f6f6f6;
    --navy: #22355e;
    --slate: #5b6270;
    --ink: #4a4d53;
    --muted: #6e7178;
    --rule: #8a8d93;
    --swoosh-gray: #7a7c80;
  }
  * { box-sizing: border-box; margin: 0; padding: 0; }
  html, body { width: 1200px; height: 800px; overflow: hidden; }
  body { background: var(--backdrop); font-family: "Lato", sans-serif; color: var(--ink); }

  .letterhead {
    position: absolute; left: 330px; top: 18px;
    width: 540px; height: 764px;
    background: var(--paper);
    box-shadow: 0 6px 18px rgba(0,0,0,0.18);
    overflow: hidden;
  }

  .brand { position: absolute; left: 40px; top: 52px; }
  .brand-row { display: flex; align-items: center; gap: 10px; }
  .brand-mark { width: 14px; height: 14px; background: var(--navy); }
  .brand-name {
    font-family: "Lato", sans-serif; font-weight: 700; color: var(--navy);
    font-size: 17px; line-height: 1.05; letter-spacing: 0.5px; text-transform: uppercase;
  }
  .brand-tagline {
    margin-top: 8px; font-size: 6.5px; letter-spacing: 2px; color: var(--slate);
    text-transform: uppercase;
  }

  .offices {
    position: absolute; left: 262px; top: 48px;
    display: flex; gap: 14px;
    font-family: "Montserrat", sans-serif; font-size: 6.2px; color: var(--ink); line-height: 1.45;
  }
  .office + .office { border-left: 1px solid var(--navy); padding-left: 12px; }
  .office-title { font-weight: 700; color: var(--navy); font-size: 6.8px; margin-bottom: 4px; }
  .office-line { display: flex; align-items: flex-start; gap: 4px; }
  .office-line svg { width: 6px; height: 6px; margin-top: 1px; flex: none; }
  .office-line.indent { padding-left: 10px; }

  .letter { position: absolute; left: 48px; top: 262px; width: 440px; }
  .letter-date { font-weight: 700; font-size: 9px; color: var(--ink); margin-bottom: 10px; }
  .recipient-name { font-weight: 700; font-size: 11.5px; color: var(--navy); }
  .recipient-role { font-size: 8px; color: var(--muted); }
  .recipient-address { font-size: 8px; color: var(--muted); margin-top: 8px; line-height: 1.35; }
  .letter-body p { font-size: 7.6px; line-height: 1.5; color: var(--muted); margin-top: 14px; text-align: justify; }
  .closing { font-size: 8px; color: var(--muted); margin-top: 22px; }
  .signature { display: block; margin-top: 20px; width: 90px; height: 26px; background: #d9dde6; border-radius: 3px; }

  .footer-wave { position: absolute; left: 0; bottom: 0; width: 540px; height: 150px; }
</style>
</head>
<body>
  <main class="letterhead">
    <header>
      <div class="brand">
        <div class="brand-row">
          <span class="brand-mark"></span>
          <div class="brand-name">Hartwell<br>Osten &amp;<br>Marlowe</div>
        </div>
        <div class="brand-tagline">The Property Damage Attorneys</div>
      </div>

      <div class="offices">
        <div class="office">
          <div class="office-title">Philadelphia Office</div>
          <div class="office-line"><svg viewBox="0 0 10 10"><rect width="10" height="10" rx="2" fill="var(--navy)"/><path d="M3 2.5l1 1.5-.7.7a4 4 0 002 2l.7-.7 1.5 1-.6 1c-3 0-5-2-5-5z" fill="#fff"/></svg>555-201-4400</div>
          <div class="office-line"><svg viewBox="0 0 10 10"><rect width="10" height="10" rx="2" fill="var(--navy)"/><rect x="2.5" y="3" width="5" height="4" fill="#fff"/></svg>555-201-4401</div>
          <div class="office-line"><svg viewBox="0 0 10 10"><rect width="10" height="10" rx="2" fill="var(--navy)"/><circle cx="5" cy="4.3" r="1.8" fill="#fff"/><path d="M3.4 5.2L5 8.2l1.6-3z" fill="#fff"/></svg>480 Market Plaza</div>
          <div class="office-line indent">Suite 310</div>
          <div class="office-line indent">Philadelphia, PA 19100</div>
        </div>
        <div class="office">
          <div class="office-title">New Jersey Office</div>
          <div class="office-line"><svg viewBox="0 0 10 10"><rect width="10" height="10" rx="2" fill="var(--navy)"/><path d="M3 2.5l1 1.5-.7.7a4 4 0 002 2l.7-.7 1.5 1-.6 1c-3 0-5-2-5-5z" fill="#fff"/></svg>555-318-7720</div>
          <div class="office-line"><svg viewBox="0 0 10 10"><rect width="10" height="10" rx="2" fill="var(--navy)"/><rect x="2.5" y="3" width="5" height="4" fill="#fff"/></svg>555-201-4401</div>
          <div class="office-line"><svg viewBox="0 0 10 10"><rect width="10" height="10" rx="2" fill="var(--navy)"/><circle cx="5" cy="4.3" r="1.8" fill="#fff"/><path d="M3.4 5.2L5 8.2l1.6-3z" fill="#fff"/></svg>72 Elm Crossing Road</div>
          <div class="office-line indent">Suite 102</div>
          <div class="office-line indent">Cherry Hill, NJ 08000</div>
        </div>
      </div>
    </header>

    <section class="letter">
      <div class="letter-date">APR - 04 - 2023</div>
      <div class="recipient-name">Mr. Daniel Reyes</div>
      <div class="recipient-role">Managing Director</div>
      <div class="recipient-address">Lakeview On Canada<br>Street 1187</div>

      <div class="letter-body">
        <p>Lorem Ipsum is simply dummy text of the printing and typesetting industry. Lorem Ipsum has been the industry's standard dummy text ever since the 1500s, when an unknown printer took a galley of type and scrambled it to make a type specimen book. It has survived not only five centuries, but also the leap into electronic typesetting, remaining essentially unchanged. It was popularised in the 1960s with the release of Letraset sheets containing Lorem Ipsum passages, and more recently with desktop publishing software like Aldus PageMaker including versions of Lorem Ipsum.</p>
        <p>Contrary to popular belief, Lorem Ipsum is not simply random text. It has roots in a piece of classical Latin literature from 45 BC, making it over 2000 years old. A Latin professor looked up one of the more obscure Latin words, consectetur, from a Lorem Ipsum passage, and going through the cites of the word in classical literature, discovered the undoubtable source. Lorem Ipsum comes from sections 1.10.32 and 1.10.33 of "de Finibus Bonorum et Malorum" (The Extremes of Good and Evil) by Cicero, written in 45 BC. This book is a treatise on the theory of ethics, very popular during the Renaissance. The first line of Lorem Ipsum, "Lorem ipsum dolor sit amet..", comes from a line in section 1.10.32.</p>
        <p>The standard chunk of Lorem Ipsum used since the 1500s is reproduced below for those interested. Sections 1.10.32 and 1.10.33 from "de Finibus Bonorum et Malorum" by Cicero are also reproduced in their exact original form, accompanied by English versions from the 1914 translation by H. Rackham.</p>
      </div>

      <div class="closing">Sincerely Yours</div>
      <span class="signature" role="img" aria-label="Handwritten signature of the sender"></span>
    </section>

    <svg class="footer-wave" viewBox="0 0 540 150" preserveAspectRatio="none" aria-hidden="true">
      <path d="M0 108 C 180 96, 380 60, 540 0 L540 8 C 380 70, 180 104, 0 116 Z" fill="var(--swoosh-gray)"/>
      <path d="M0 118 C 180 106, 380 76, 540 14 L540 150 L0 150 Z" fill="var(--navy)"/>
    </svg>
  </main>
</body>
</html>
```